Brightfield Co Trade Show Flyer

We need a brochure design (8.5 x 11) Info in the design (refer to rough draft I drew on Paper): "#1 selling tool to aquire new franchisees has been video testimonials" - Martin L. Crowe, C.E.O Tovik Smoothie Franchise Testimonials - Let your franchisees do the selling for you. Franchisee testimonial: $10,000 / per Franchisee Includes: • 2 minute Video • 1 minute add for your franchise's location • Concept creation • Communication with franchisee • Travel to their location • All rental equipment • 1 round of corrections • Animated logo • Licensed music ******* For 25% Discount section (next to middle box), please put the "Outlet Summit Logo" Great to use on all your social media (USE logos and icons) • Website • YouTube • LinkedIn • Facebook • Instagram • Twitter • Phone calls • Emails • In person meetings Some of our clients: (use the logos I uploaded - in round boxes as in draft) LOGO (Brightfield Franchise Testimonial) www.brightfieldvoices.example (866) 555-0172

Target Market(s)

Franchise owners

Colors

Designer to choose colors to be used in the design.

Requirements

```html
<!DOCTYPE html>
<html lang="en">
<head>
<meta charset="utf-8">
<title>Brightfield Co Trade Show Flyer</title>
<link rel="stylesheet" href="https://fonts.googleapis.com/css2?family=Montserrat:ital,wght@0,500;0,600;0,700;0,800;0,900;1,700&display=swap">
<style>
  :root {
    --stage: #d9d9dc;
    --paper-top: #c9cbd1;
    --paper-mid: #eceef1;
    --royal: #3a4fb3;
    --royal-dark: #2c3d94;
    --ink: #1e1f22;
    --night: #1d1e21;
    --night-2: #26272b;
    --teal: #1aa99a;
    --white: #ffffff;
    --muted: #c9cbd3;
  }
  * { box-sizing: border-box; margin: 0; padding: 0; }
  html, body { width: 1200px; height: 798px; overflow: hidden; }
  body {
    background: var(--stage);
    font-family: "Montserrat", Arial, sans-serif;
    color: var(--ink);
    position: relative;
  }
  .flyer {
    position: absolute;
    left: 330px; top: 19px;
    width: 540px; height: 760px;
    overflow: hidden;
    background: linear-gradient(180deg, var(--paper-top) 0%, var(--paper-mid) 45%, #f4f5f7 70%);
    box-shadow: 0 6px 20px rgba(0,0,0,.18);
  }
  .office-backdrop {
    position: absolute; inset: 0 0 300px 0;
    background: linear-gradient(160deg, rgba(160,163,175,.55) 0%, rgba(230,232,236,.2) 55%, rgba(255,255,255,0) 100%);
  }
  .brand {
    position: absolute; left: 383px; top: 28px; width: 134px;
    text-align: center;
  }
  .brand-dot {
    display: block; width: 34px; height: 34px; margin: 0 auto 8px;
    border-radius: 50%; background: var(--ink);
  }
  .brand-name { font-weight: 900; font-size: 19px; letter-spacing: .5px; line-height: 1; }
  .brand-sub { font-weight: 600; font-size: 6.5px; margin-top: 4px; letter-spacing: .2px; }
  .quote {
    position: absolute; left: 27px; top: 62px; width: 290px;
    font-style: italic; font-weight: 700; font-size: 8px; line-height: 1.3;
    text-transform: uppercase; letter-spacing: -.2px;
  }
  .headline {
    position: absolute; left: 24px; top: 88px;
    color: var(--royal); font-weight: 900; font-size: 45px;
    line-height: .92; letter-spacing: -1.4px; text-transform: uppercase;
    z-index: 2;
  }
  .tagline {
    position: absolute; left: 26px; top: 180px;
    font-weight: 800; font-size: 12.5px; text-transform: uppercase; letter-spacing: -.4px;
    z-index: 2;
  }
  .price {
    position: absolute; left: 24px; top: 226px;
    font-weight: 800; font-size: 9.5px; line-height: 1.35; text-transform: uppercase; letter-spacing: -.3px;
  }
  .includes {
    position: absolute; left: 22px; top: 252px; width: 230px;
    list-style: none;
    display: grid; grid-template-columns: 110px 118px; row-gap: 14px;
    z-index: 2;
  }
  .includes li {
    display: flex; align-items: center; gap: 4px; min-height: 24px;
    font-weight: 600; font-size: 7.3px; line-height: 1.05; text-transform: uppercase;
  }
  .includes svg { flex: 0 0 auto; width: 19px; height: 21px; }
  .portrait {
    position: absolute; left: 262px; top: 124px; width: 250px; height: 440px;
    background: linear-gradient(180deg, #d6d9e2 0%, #cfd3de 28%, #2e3868 50%, #262d57 100%);
    clip-path: polygon(42% 0, 100% 0, 100% 100%, 0 100%, 0 36%, 42% 30%);
    opacity: .9;
  }
  .base { position: absolute; left: 0; top: 420px; width: 540px; height: 340px; }
  .promo {
    position: absolute; left: 34px; top: 420px; width: 170px; height: 134px;
    color: var(--ink);
  }
  .promo-blob { position: absolute; inset: 0; }
  .promo-label { position: absolute; left: 22px; top: 22px; font-weight: 800; font-size: 8.5px; text-transform: uppercase; }
  .promo-pct { position: absolute; left: 20px; top: 34px; font-weight: 900; font-size: 38px; letter-spacing: -2px; line-height: 1; }
  .promo-for { position: absolute; left: 110px; top: 36px; font-weight: 900; font-size: 11px; text-transform: uppercase; }
  .promo-partner { position: absolute; left: 30px; top: 84px; width: 90px; font-weight: 800; font-size: 7.5px; color: var(--white); line-height: 1.1; }
  .channels {
    position: absolute; left: 24px; top: 582px;
    color: var(--white); font-weight: 800; font-size: 9px; text-transform: uppercase; letter-spacing: -.2px;
  }
  .channel-row { position: absolute; left: 24px; top: 605px; display: flex; gap: 5px; }
  .channel {
    width: 27px; height: 27px; border-radius: 50%;
    background: var(--royal); display: flex; align-items: center; justify-content: center;
  }
  .channel.red { background: #d8352d; }
  .channel.sky { background: #2f9be0; }
  .channel.pink { background: #d9468a; }
  .channel svg { width: 14px; height: 14px; }
  .trusted {
    position: absolute; left: 80px; top: 652px; width: 100px; text-align: center;
    color: var(--white); font-weight: 800; font-size: 9px; text-transform: uppercase;
  }
  .client-row { position: absolute; left: 20px; top: 675px; display: flex; gap: 4px; }
  .client { width: 34px; height: 34px; border-radius: 50%; background: var(--white); }
  .client.yellow { background: #ecd21c; }
  .client.teal { background: var(--teal); }
  .call { position: absolute; left: 258px; top: 606px; display: flex; align-items: center; gap: 6px; }
  .call-icon { width: 18px; height: 40px; }
  .call-label { color: var(--white); font-weight: 800; font-size: 14px; text-transform: uppercase; line-height: 1; }
  .call-number { color: var(--royal); font-weight: 800; font-size: 21px; line-height: 1.1; letter-spacing: .3px; }
  .site-pill {
    position: absolute; left: 252px; top: 665px; width: 254px; height: 25px;
    border-radius: 13px; background: var(--royal);
    color: var(--white); font-weight: 700; font-size: 7.2px; letter-spacing: 2.3px;
    display: flex; align-items: center; justify-content: center; text-transform: uppercase;
  }
  .contact { position: absolute; left: 296px; top: 713px; display: flex; align-items: center; gap: 8px; }
  .contact svg { width: 22px; height: 22px; }
  .contact p { color: var(--white); font-weight: 500; font-size: 8.5px; line-height: 1.45; }
</style>
</head>
<body>
<main class="flyer">
  <div class="office-backdrop" role="img" aria-label="Bright modern office interior with ceiling lights"></div>

  <div class="portrait" role="img" aria-label="Young businessman in a navy suit and white shirt, hands in pockets"></div>

  <div class="brand">
    <span class="brand-dot"></span>
    <div class="brand-name">BRIGHTFIELD</div>
    <div class="brand-sub">FRANCHISE TESTIMONIALS</div>
  </div>

  <p class="quote">"#1 selling tool to aquire new franchisees has been video testimonials" – Martin L. Crowe, C.E.O Tovik Smoothie</p>

  <h1 class="headline">Franchise<br>Testimonials</h1>
  <p class="tagline">Let your franchisees do the selling for you</p>

  <p class="price">Franchisee testimonial: $10,000<br>per franchisee includes:</p>

  <ul class="includes">
    <li><svg viewBox="0 0 19 21"><polygon points="9.5,0 19,5.25 19,15.75 9.5,21 0,15.75 0,5.25" fill="#3a4fb3"/></svg>2 minute video</li>
    <li><svg viewBox="0 0 19 21"><polygon points="9.5,0 19,5.25 19,15.75 9.5,21 0,15.75 0,5.25" fill="#3a4fb3"/></svg>Communication with franchisee</li>
    <li><svg viewBox="0 0 19 21"><polygon points="9.5,0 19,5.25 19,15.75 9.5,21 0,15.75 0,5.25" fill="#3a4fb3"/></svg>1 minute add for your franchise's location</li>
    <li><svg viewBox="0 0 19 21"><polygon points="9.5,0 19,5.25 19,15.75 9.5,21 0,15.75 0,5.25" fill="#3a4fb3"/></svg>Travel to their location</li>
    <li><svg viewBox="0 0 19 21"><polygon points="9.5,0 19,5.25 19,15.75 9.5,21 0,15.75 0,5.25" fill="#3a4fb3"/></svg>Concept creation</li>
    <li><svg viewBox="0 0 19 21"><polygon points="9.5,0 19,5.25 19,15.75 9.5,21 0,15.75 0,5.25" fill="#3a4fb3"/></svg>All rental equipment</li>
    <li><svg viewBox="0 0 19 21"><polygon points="9.5,0 19,5.25 19,15.75 9.5,21 0,15.75 0,5.25" fill="#3a4fb3"/></svg>1 round of corrections</li>
    <li><svg viewBox="0 0 19 21"><polygon points="9.5,0 19,5.25 19,15.75 9.5,21 0,15.75 0,5.25" fill="#3a4fb3"/></svg>Animated logo</li>
  </ul>

  <svg class="base" viewBox="0 0 540 340" preserveAspectRatio="none" aria-hidden="true">
    <path d="M0 17 C120 30 250 90 330 130 C400 160 470 60 540 37 L540 340 L0 340 Z" fill="#3a4fb3"/>
    <path d="M0 70 C120 80 240 140 330 150 C420 160 480 90 540 70 L540 340 L0 340 Z" fill="#1d1e21"/>
    <path d="M0 200 L110 160 L190 230 L300 190 L420 240 L540 180 L540 340 L0 340 Z" fill="#26272b" opacity=".7"/>
  </svg>

  <div class="promo">
    <svg class="promo-blob" viewBox="0 0 170 134" aria-hidden="true">
      <path d="M30 8 C70 0 120 4 150 20 C172 40 165 80 150 100 C130 125 80 134 40 128 C10 122 0 90 6 60 C10 35 12 14 30 8 Z" fill="#1aa99a"/>
    </svg>
    <span class="promo-label">Licensed music</span>
    <span class="promo-pct">25%</span>
    <span class="promo-for">For</span>
    <span class="promo-partner">Outlet Summit</span>
  </div>

  <p class="channels">Use your testimonials everywhere</p>
  <div class="channel-row">
    <span class="channel red"></span>
    <span class="channel sky"></span>
    <span class="channel"></span>
    <span class="channel"></span>
    <span class="channel"><svg viewBox="0 0 24 24"><path d="M6 2 L10 6 L8 9 C9 12 12 15 15 16 L18 14 L22 18 L19 22 C10 21 3 14 2 5 Z" fill="none" stroke="#fff" stroke-width="2"/></svg></span>
    <span class="channel"><svg viewBox="0 0 24 24"><rect x="2" y="5" width="20" height="14" fill="none" stroke="#fff" stroke-width="2"/><path d="M2 5 L12 13 L22 5" fill="none" stroke="#fff" stroke-width="2"/></svg></span>
    <span class="channel pink"></span>
  </div>

  <p class="trusted">Trusted by :</p>
  <div class="client-row">
    <span class="client"></span>
    <span class="client"></span>
    <span class="client"></span>
    <span class="client"></span>
    <span class="client yellow"></span>
    <span class="client teal"></span>
  </div>

  <div class="call">
    <svg class="call-icon" viewBox="0 0 18 40" aria-hidden="true"><path d="M14 2 C4 8 2 30 14 38 L17 33 C10 28 10 12 17 7 Z" fill="#3a4fb3"/></svg>
    <div>
      <div class="call-label">Call us now</div>
      <div class="call-number">(866) 555-0172</div>
    </div>
  </div>

  <div class="site-pill">www.brightfieldvoices.example</div>

  <div class="contact">
    <svg viewBox="0 0 22 22" aria-hidden="true"><circle cx="11" cy="11" r="11" fill="#3a4fb3"/><circle cx="11" cy="11" r="6" fill="none" stroke="#fff" stroke-width="1.2"/><ellipse cx="11" cy="11" rx="2.6" ry="6" fill="none" stroke="#fff" stroke-width="1.2"/><line x1="5" y1="11" x2="17" y2="11" stroke="#fff" stroke-width="1.2"/></svg>
    <p>testimonials@brightfieldco.example<br>www.brightfieldvoices.example</p>
  </div>
</main>
</body>
</html>
```